Brivan Learning Web Design Project

Who We are:
Brivan Learning is education information portal/ magazine, providing information about the Chinese and International education markets. Our aim is to help school principals improve there curriculum, and parents in understanding this curriculum.

Project Brief:
The site will include education news updates, educational services, curriculum developments and overseas study. We hope the site represents the cross cultural bridge between the west and east. The site will cover both the Sciences and Arts.

Note:
The logo design competition is also underway so we only need the website design

What We want:
This competition is for Design only no coding!
Design a home page based on Template 1,2 or 3. I only need to select one.
The design of an article page.

Optional
Design a Microsoft Windows metro style splash page.

Sites We like:
http://www.qz.com.cn/wordsparrow/default.aspx
http://www.velmaracademicpost.co.uk/
http://pvro.orbalinkstudy.net/

Template Explanations:
Template 1-
The main information has a dynamic sliding category view that when clicked displays the relevant info.
In addition to the main upper menu it also has a left hand sliding menu that pops out on click or gesture

Template 2-
Has limited number of Articles most of the menus are drop downs from the top menu

Template 3-
No Top menu

Target Market(s)

Teachers, principals and parents

Industry/Entity Type

Education

Requirements
Should not have
• kindergarten preschool feel

```html
<!DOCTYPE html>
<html lang="en">
<head>
<meta charset="utf-8">
<title>Brivan Learning</title>
<link rel="stylesheet" href="https://fonts.googleapis.com/css2?family=Open+Sans:wght@400;600;700&family=Arimo:wght@400;700&family=PT+Sans&display=swap">
<style>
:root{
  --brand-red:#e0242a;
  --brand-blue:#1d5a8c;
  --hero-top:#0470b3;
  --hero-bottom:#079ccc;
  --ink:#333;
  --ink-soft:#555;
  --muted:#999;
  --nav-active:#3a6fd8;
  --card-bg:#f0f0f0;
  --card-line:#e2e2e2;
  --course-title:#4a7eab;
  --footer-bg:#f8f5f5;
  --bar-bg:#333;
  --white:#fff;
}
*{margin:0;padding:0;box-sizing:border-box}
html,body{width:1200px;height:900px;overflow:hidden;background:var(--white)}
body{position:relative;font-family:Arimo,Arial,sans-serif;color:var(--ink)}
.abs{position:absolute}

/* header */
.brand{left:308px;top:0;width:124px;height:76px}
.brand-mark{left:50px;top:2px;width:40px;height:40px;border-radius:50%;background:var(--brand-blue)}
.brand-name{left:0;top:49px;width:124px;text-align:center;font-size:14px;color:var(--brand-red);letter-spacing:.2px}
.search{left:745px;top:7px;width:156px;height:18px;display:flex;border:1px solid #ddd}
.search-input{flex:1;font:italic 7px Georgia,serif;color:var(--muted);padding:5px 7px;background:#fff}
.search-btn{width:31px;background:#eee;border-left:1px solid #ddd;font-size:7px;color:#444;text-align:center;line-height:16px}
.nav{left:506px;top:45px;display:flex}
.nav-item{text-align:center;padding:0 13px;border-left:1px solid #e4e4e4;height:22px}
.nav-item:first-child{border-left:none}
.nav-title{font-size:8px;color:var(--ink);line-height:13px}
.nav-item.is-active .nav-title{color:var(--nav-active)}
.nav-sub{font:italic 6.5px Georgia,serif;color:#aaa}

/* hero */
.hero{left:277px;top:94px;width:646px;height:188px;background:linear-gradient(180deg,var(--hero-top) 0%,var(--hero-top) 35%,var(--hero-bottom) 100%)}

/* featured */
.feature{top:298px;width:292px;height:145px;background:var(--card-bg);border:1px solid var(--card-line);box-shadow:0 0 2px rgba(0,0,0,.08)}
.feature-title{left:13px;top:8px;font:400 12px "Open Sans",sans-serif;color:#444}
.feature-byline{right:10px;top:7px;font-size:6px;color:#555}
.feature-image{left:13px;top:26px;width:114px;height:113px;background:var(--brand-blue)}
.feature-text{left:135px;top:26px;width:148px;font-size:7px;line-height:10.7px;color:#444}
.feature-meta{left:135px;top:116px;width:148px;border-top:1px solid #e0e0e0;padding-top:11px;font-size:6px;color:#555;display:flex;gap:10px;padding-left:3px}
.dot{display:inline-block;width:6px;height:5px;background:#999;border-radius:2px;margin-right:4px;vertical-align:middle}

/* courses */
.course-image{top:489px;width:182px;height:113px;background:var(--brand-blue);box-shadow:0 2px 2px rgba(0,0,0,.12)}
.course-title{font:700 19px "Open Sans",sans-serif;color:var(--course-title);letter-spacing:-.3px}
.course-sub{font:400 9px "Open Sans",sans-serif;color:#444}
.course-text{width:186px;font:10.3px/11.8px "PT Sans",Tahoma,sans-serif;color:#333}

/* footer */
.footer{left:277px;top:752px;width:646px;height:120px;background:var(--footer-bg)}
.footer-heading{font:400 13px "Open Sans",sans-serif;color:#333}
.count{font:7px Georgia,serif;color:#999;display:flex;align-items:center;gap:4px}
.count-icon{width:9px;height:9px;border-radius:50%}
.social{top:819px;width:17px;height:17px}
.links{font-size:6.8px;line-height:10.7px;color:#222}
.foot-mark{left:821px;top:761px;width:28px;height:28px;border-radius:50%;background:var(--brand-blue)}
.foot-name{left:790px;top:796px;width:94px;text-align:center;font-size:10px;color:var(--brand-red)}
.address{left:794px;top:818px;font-size:7px;line-height:11px;color:#111}
.bar{left:277px;top:872px;width:646px;height:28px;background:var(--bar-bg);color:var(--white);font-size:7.5px;text-align:center;line-height:31px}
</style>
</head>
<body>

<header>
  <div class="abs brand">
    <span class="abs brand-mark"></span>
    <span class="abs brand-name">BRIVAN LEARNING</span>
  </div>
  <div class="abs search">
    <span class="search-input">to search, type and hit enter</span>
    <span class="search-btn">Search</span>
  </div>
  <nav class="abs nav">
    <div class="nav-item is-active"><div class="nav-title">Home</div><div class="nav-sub">welcome</div></div>
    <div class="nav-item"><div class="nav-title">About us</div><div class="nav-sub">now on site</div></div>
    <div class="nav-item"><div class="nav-title">Some menu</div><div class="nav-sub">description</div></div>
    <div class="nav-item"><div class="nav-title">Another menu</div><div class="nav-sub">Description</div></div>
    <div class="nav-item"><div class="nav-title">Blogs</div><div class="nav-sub">some description</div></div>
    <div class="nav-item"><div class="nav-title">contact us</div><div class="nav-sub">We glad to assist</div></div>
  </nav>
</header>

<div class="abs hero" role="img" aria-label="Feature slideshow banner"></div>

<article class="abs feature" style="left:298px">
  <h2 class="abs feature-title">Featured article one</h2>
  <span class="abs feature-byline">By Marcus Hollen</span>
  <div class="abs feature-image" role="img" aria-label="Article photo"></div>
  <p class="abs feature-text">Lorem ipsum dolor sit amet, consectetuer adipiscing elit, sed diam nonummy nibh euismod tincidunt ut laoreet dolore magna aliquam erat volutpat. Ut wisi enim ad minim veniam, quis nostrud exerci tation ullamcorper suscipit lobortis nisl ut aliquip ex ea commodo consequat.Lorem ipsum dolor sit amet, consectetuer adipiscing elit, sed diam nonummy nibh euismod tincidunt ut</p>
  <div class="abs feature-meta"><span><i class="dot"></i>15 Comments</span><span>+ Share</span><span><i class="dot"></i>27 July 2013</span></div>
</article>

<article class="abs feature" style="left:609px">
  <h2 class="abs feature-title">Featured article two</h2>
  <span class="abs feature-byline">By Marcus Hollen</span>
  <div class="abs feature-image" role="img" aria-label="Article photo"></div>
  <p class="abs feature-text">Lorem ipsum dolor sit amet, consectetuer adipiscing elit, sed diam nonummy nibh euismod tincidunt ut laoreet dolore magna aliquam erat volutpat. Ut wisi enim ad minim veniam, quis nostrud exerci tation ullamcorper suscipit lobortis nisl ut aliquip ex ea commodo consequat.Lorem ipsum dolor sit amet, consectetuer adipiscing elit, sed diam nonummy nibh euismod tincidunt ut</p>
  <div class="abs feature-meta"><span><i class="dot"></i>15 Comments</span><span>+ Share</span><span><i class="dot"></i>27 July 2013</span></div>
</article>

<section>
  <div class="abs course-image" style="left:300px" role="img" aria-label="Course one photo"></div>
  <h3 class="abs course-title" style="left:302px;top:614px">Course one</h3>
  <p class="abs course-sub" style="left:304px;top:640px">Market Research</p>
  <p class="abs course-text" style="left:304px;top:657px">Lorem ipsum dolor sit amet, consectetuer adipiscing elit, sed diam nonummy nibh euismod tincidunt ut laoreet dolore magna aliquam erat volutpat. Ut wisi enim ad minim veniam, quis nostrud exerci tation ullamcorper suscipit lobortis nisl ut aliquip</p>

  <div class="abs course-image" style="left:507px" role="img" aria-label="Course two photo"></div>
  <h3 class="abs course-title" style="left:505px;top:616px">Course two</h3>
  <p class="abs course-sub" style="left:508px;top:640px">Management</p>
  <p class="abs course-text" style="left:508px;top:660px">Lorem ipsum dolor sit amet, consectetuer adipiscing elit, sed diam nonummy nibh euismod tincidunt ut laoreet dolore magna aliquam erat volutpat. Ut wisi enim ad minim veniam, quis nostrud exerci tation ullamcorper suscipit lobortis nisl ut aliquip</p>

  <div class="abs course-image" style="left:717px" role="img" aria-label="Course three photo"></div>
  <h3 class="abs course-title" style="left:715px;top:616px">Course three</h3>
  <p class="abs course-sub" style="left:718px;top:640px">Science &amp; arts</p>
  <p class="abs course-text" style="left:718px;top:660px">Lorem ipsum dolor sit amet, consectetuer adipiscing elit, sed diam nonummy nibh euismod tincidunt ut laoreet dolore magna aliquam erat volutpat. Ut wisi enim ad minim veniam, quis nostrud exerci tation ullamcorper suscipit lobortis nisl ut aliquip</p>
</section>

<footer>
  <div class="abs footer"></div>
  <h4 class="abs footer-heading" style="left:300px;top:765px">Follow us</h4>
  <div class="abs count" style="left:300px;top:793px"><i class="count-icon" style="background:#f0902a"></i>3042</div>
  <div class="abs count" style="left:343px;top:793px"><i class="count-icon" style="background:#3a9ad8"></i>301</div>
  <div class="abs count" style="left:389px;top:793px"><i class="count-icon" style="background:#2e68c8"></i>800</div>
  <span class="abs social" style="left:299px;background:#3b5a98"></span>
  <span class="abs social" style="left:321px;background:#5aaee0"></span>
  <span class="abs social" style="left:344px;background:#f08a24"></span>
  <span class="abs social" style="left:368px;background:#4bb4d8"></span>
  <span class="abs social" style="left:391px;background:#1b78b4"></span>

  <h4 class="abs footer-heading" style="left:440px;top:765px">Contents list</h4>
  <div class="abs links" style="left:442px;top:787px">Lorem ipsum dolor sit amet<br>Lorem ipsum dolor sit amet<br>Lorem ipsum dolor sit amet<br>Lorem ipsum dolor sit amet<br>Lorem ipsum dolor sit amet<br>Lorem ipsum dolor sit amet</div>
  <div class="abs links" style="left:550px;top:787px">Lorem ipsum dolor sit amet<br>Lorem ipsum dolor sit amet<br>Lorem ipsum dolor sit amet<br>Lorem ipsum dolor sit amet<br>Lorem ipsum dolor sit amet<br>Lorem ipsum dolor sit amet</div>
  <div class="abs links" style="left:662px;top:787px">Lorem ipsum dolor sit amet<br>Lorem ipsum dolor sit amet<br>Lorem ipsum dolor sit amet<br>Lorem ipsum dolor sit amet<br>Lorem ipsum dolor sit amet<br>Lorem ipsum dolor sit amet</div>

  <span class="abs foot-mark"></span>
  <span class="abs foot-name">BRIVAN LEARNING</span>
  <address class="abs address" style="font-style:normal">01 Lorem ipsum dolor sit amet 1<br>12345 NJ Lorem ipsum dolor.<br>Phone: (+91) 98 40 215736</address>

  <div class="abs bar">© 2013 Brivan Learning</div>
</footer>

</body>
</html>
```